We are a doctors medical practice
I need the business card to be eye catching and memorable,
to reflect professionalism, yet also warmth and care

the numbers need to be easy to see, for the elderly

and the logo also in a location that is large enough to see and be eye catching

Back of card:
opening hours:
Mon- Fri 8.30am to 6pm
Sat 9am to 4pm

rows for appontments, date and time
Updates

HiĀ 

Modification to company name

BROOKVALE KINDRED HEALTH MEDICAL PRACTICE

Thanks
Marla

Reason: I am look for a unique design that also fulfils the design brief

I have attempted to post a .eps and .ai file of the logo

Target Market(s)

needs to appeal to the majority, mainly adults

Industry/Entity Type

Medical

Contact Information for Business Card

company name: Brookvale Kindred Health Medical Practice
Name: Dr Marla Vossberg-Tait
Qualifications: MBBS, Bsci(med), FRACGP, DCH, SH&FPA, Dip Derm
Address: Shop 3/41-43 Quorrow St, Brookvale 2940
Ph: 02 9418 3052
Fax: 02 9461 8824

Requirements
Nice to have
• I like balance
gold/ silver incorporated, as well as the other colours in the logo- but not limited to these colours
a "medical" feel
Should not have
• dark or strong colours

```html
<!DOCTYPE html>
<html lang="en">
<head>
<meta charset="utf-8">
<title>Brookvale Kindred Health Medical Practice – Business Card</title>
<link rel="stylesheet" href="https://fonts.googleapis.com/css2?family=Source+Sans+3:wght@400;600;700;900&display=swap">
<style>
  :root {
    --backdrop: #ecebe8;
    --card-white: #ffffff;
    --gold: #fbb616;
    --gold-deep: #f2a50c;
    --gold-soft: #fddb7e;
    --navy: #1d3266;
    --crimson: #a3161b;
    --ink: #1d1a14;
    --sage: #a9b93a;
    --sky: #5aa9d6;
    --mist-top: #ffffff;
    --mist-bottom: #d9d9d9;
    --rule: #3a3a3a;
  }
  * { box-sizing: border-box; margin: 0; padding: 0; }
  html, body {
    width: 1200px; height: 900px; overflow: hidden;
    background: var(--backdrop);
    font-family: "Source Sans 3", "Segoe UI", sans-serif;
    color: var(--ink);
  }
  .sheet { position: relative; width: 1200px; height: 900px; }
  .card {
    position: absolute; left: 240px; width: 720px; height: 411px;
    overflow: hidden; border-radius: 3px;
    box-shadow: 0 4px 14px rgba(0,0,0,0.18);
  }
  /* ---------- Front ---------- */
  .card-front { top: 26px; background: var(--card-white); }
  .front-header {
    position: absolute; inset: 0 0 auto 0; height: 112px;
    display: flex; align-items: center; gap: 18px; padding-left: 34px;
  }
  .brand-dot {
    width: 70px; height: 70px; border-radius: 50%;
    border: 5px solid var(--sky); flex: none;
  }
  .brand-name {
    font-weight: 700; font-size: 27px; letter-spacing: 0.3px; color: var(--navy);
  }
  .front-body {
    position: absolute; left: 0; right: 0; top: 112px; bottom: 0;
    background: linear-gradient(180deg, var(--gold) 0%, var(--gold-deep) 100%);
  }
  .illustration {
    position: absolute; left: 18px; top: 28px; width: 290px; height: 290px;
    border-radius: 50%;
    background: radial-gradient(circle at 45% 45%, #fee4a0 0%, var(--gold-soft) 60%, #f3c55a 100%);
    box-shadow: 10px -6px 0 4px rgba(169,185,58,0.7);
  }
  .practitioner { position: absolute; left: 336px; top: 20px; right: 20px; }
  .practitioner-name { font-weight: 900; font-size: 33px; color: var(--crimson); line-height: 1.05; }
  .credentials { font-weight: 700; font-size: 17px; line-height: 1.3; margin-top: 6px; }
  .contact { margin-top: 34px; display: grid; grid-template-columns: 86px 16px 1fr; row-gap: 2px;
             font-weight: 600; font-size: 21px; line-height: 1.2; }
  /* ---------- Back ---------- */
  .card-back { top: 463px; background: linear-gradient(180deg, var(--mist-top) 30%, var(--mist-bottom) 100%); }
  .hours-band {
    position: absolute; inset: 0 0 auto 0; height: 118px;
    background: var(--gold); display: flex; align-items: center; padding-left: 40px; gap: 22px;
  }
  .hours-title { font-weight: 700; font-size: 33px; white-space: nowrap; }
  .hours-list { font-weight: 700; font-size: 27px; line-height: 1.15; }
  .hours-list span { display: block; }
  .hours-list span + span { padding-left: 26px; }
  .faint-ring {
    position: absolute; right: 70px; top: 150px; width: 240px; height: 240px;
    border-radius: 50%; border: 12px solid rgba(90,169,214,0.18);
  }
  .appointments { position: absolute; left: 40px; right: 40px; top: 130px; bottom: 18px; }
  .appointments-head { display: flex; justify-content: space-between; font-weight: 700; font-size: 18px; }
  .appointment-row { height: 30px; border-bottom: 2px dotted var(--rule); }
</style>
</head>
<body>
<main class="sheet">
  <section class="card card-front" aria-label="Business card front">
    <header class="front-header">
      <span class="brand-dot" aria-hidden="true"></span>
      <h1 class="brand-name">BROOKVALE KINDRED HEALTH MEDICAL PRACTICE</h1>
    </header>
    <div class="front-body">
      <div class="illustration" role="img" aria-label="Winged caduceus with stethoscope held above open hands, inside a gold circle with a green arc"></div>
      <div class="practitioner">
        <h2 class="practitioner-name">Dr Marla Vossberg-Tait</h2>
        <p class="credentials">MBBS, Bsci(med), FRACGP,<br>DCH, SH&amp;FPA, Dip Derm</p>
        <div class="contact">
          <span>Tel</span><span>:</span><span>02 9418 3052</span>
          <span>Fax</span><span>:</span><span>02 9461 8824</span>
          <span>Address</span><span>:</span><span>Shop 3/41-43 Quorrow St,<br>Brookvale 2940</span>
        </div>
      </div>
    </div>
  </section>

  <section class="card card-back" aria-label="Business card back">
    <div class="hours-band">
      <h2 class="hours-title">OPENING HOURS:</h2>
      <p class="hours-list"><span>Mon- Fri 8.30am to 6pm</span><span>Sat 9am to 4pm</span></p>
    </div>
    <span class="faint-ring" aria-hidden="true"></span>
    <div class="appointments">
      <div class="appointments-head"><span>Appontments</span><span>Date &amp; Time</span></div>
      <div class="appointment-row"></div>
      <div class="appointment-row"></div>
      <div class="appointment-row"></div>
      <div class="appointment-row"></div>
      <div class="appointment-row"></div>
      <div class="appointment-row"></div>
      <div class="appointment-row"></div>
      <div class="appointment-row"></div>
    </div>
  </section>
</main>
</body>
</html>
```